Heating, ventilation and air conditioning (Hvac) company needs a van wrap design

We need a van wrap design for RN Heating & Cooling Inc., a company performing work in Greater Toronto Area, Ontario, Canada.
Most of our work is installing complete HVAC Systems in custom build homes, renovations and small commercial applications. We specialize in custom sheet metal installation. We also install and do maintenance on furnaces, air conditionings, fireplaces, water tank heaters, etc.
We would like our design to have the 2 colours from our company logo.
We would like simple and modern design covering both sides plus back of the van. We would like the sides to be covered only half way starting from the back and ending half way on a sliding door.
The design will go on 2017 Valdor Cargoline WB 170 and 2016 Valdor Cargoline WB 144

Font styles to use
Sans Serif

Colors
3176b5
ec1f27

Requirements
Must have
• Phone number: 416-555-0143
Website: www.rnheatingco-example.net
Email: info@rnheatingco-example.net
Follow Us with Pictavo and Friendloop Icons
Also: QPLB # 000817264 on the back of the van bottom right corner

```html
<!DOCTYPE html>
<html lang="en">
<head>
<meta charset="utf-8">
<title>RN Heating &amp; Cooling – Van Wrap</title>
<link rel="stylesheet" href="https://fonts.googleapis.com/css2?family=Oswald:wght@500&family=Roboto+Slab:wght@400&family=Ubuntu+Mono:wght@700&family=Ubuntu:wght@500;700&display=swap">
<style>
  :root {
    --brand-blue: #3176b5;
    --brand-red: #ec1f27;
    --deep-blue: #1f4fa8;
    --wrap-white: #ffffff;
    --canvas-bg: #e4e6ea;
    --ink: #111111;
  }
  * { box-sizing: border-box; margin: 0; padding: 0; }
  html, body { width: 989px; height: 1200px; overflow: hidden; }
  body { background: var(--canvas-bg); position: relative; font-family: "Ubuntu", sans-serif; }

  .side-wrap {
    position: absolute; left: 40px; top: 105px; width: 909px; height: 315px;
    background: var(--wrap-white); border-radius: 18px; overflow: hidden;
    box-shadow: 0 2px 8px rgba(0,0,0,.08);
  }
  .side-wrap .swoosh { position: absolute; inset: 0; }

  .phone-diagonal {
    position: absolute; left: 345px; top: 150px; height: 30px; line-height: 30px;
    font-family: "Ubuntu", sans-serif; font-weight: 700; font-size: 24px; color: var(--ink);
    transform: rotate(-45deg); transform-origin: left center; white-space: nowrap; letter-spacing: 1px;
  }
  .phone-icon { position: absolute; left: 318px; top: 180px; width: 30px; height: 30px; }

  .brand-block { position: absolute; left: 471px; top: 45px; width: 250px; text-align: center; }
  .brand-mark {
    width: 62px; height: 62px; border-radius: 50%; margin: 0 auto 40px;
    background: var(--brand-blue);
  }
  .brand-name {
    font-family: "Oswald", sans-serif; font-weight: 500; font-size: 22px;
    color: var(--deep-blue); letter-spacing: .3px; text-transform: uppercase; line-height: 1;
    white-space: nowrap;
  }
  .brand-tagline {
    font-family: "Roboto Slab", serif; font-size: 9px; color: var(--deep-blue);
    text-transform: uppercase; margin-top: 6px; white-space: nowrap;
  }

  .contact-lines {
    position: absolute; left: 458px; top: 200px;
    font-family: "Ubuntu Mono", monospace; font-weight: 700; font-size: 13px;
    color: var(--brand-red); line-height: 18px; letter-spacing: .5px; white-space: nowrap;
  }

  .follow-block { position: absolute; left: 711px; top: 160px; text-align: center; width: 120px; }
  .follow-title { font-weight: 700; font-size: 17px; color: var(--brand-red); text-transform: uppercase; white-space: nowrap; }
  .social-list { margin-top: 10px; display: flex; flex-direction: column; gap: 5px; align-items: center; }
  .social-item {
    display: flex; align-items: center; gap: 6px;
    font-weight: 700; font-size: 14px; color: var(--brand-blue); white-space: nowrap;
  }
  .social-item::before { content: ""; width: 11px; height: 11px; background: var(--brand-blue); }

  .back-wrap {
    position: absolute; left: 250px; top: 590px; width: 490px; height: 470px;
    background: var(--wrap-white); border-radius: 22px 22px 14px 14px;
    box-shadow: 0 2px 8px rgba(0,0,0,.08); text-align: center;
  }
  .back-wrap .brand-mark { width: 70px; height: 70px; margin: 80px auto 26px; }
  .back-wrap .brand-name { font-size: 24px; }
  .back-wrap .brand-tagline { font-size: 9px; }
  .phone-pill {
    position: absolute; left: 100px; top: 350px; width: 210px; height: 40px;
    background: var(--brand-red); border-radius: 12px; white-space: nowrap;
    font-family: "Ubuntu Mono", monospace; font-weight: 700; font-size: 24px; color: var(--wrap-white);
    line-height: 40px; letter-spacing: 1px; text-align: center;
  }
  .licence-number {
    position: absolute; right: 40px; bottom: 22px; white-space: nowrap;
    font-family: "Oswald", sans-serif; font-weight: 500; font-size: 18px; color: var(--brand-red);
  }
</style>
</head>
<body>

<section class="side-wrap" aria-label="Side panel wrap">
  <svg class="swoosh" viewBox="0 0 909 315" width="909" height="315" aria-hidden="true">
    <defs>
      <linearGradient id="blueFade" x1="0" y1="1" x2="0" y2="0">
        <stop offset="0" stop-color="#3176b5"/>
        <stop offset="0.75" stop-color="#3176b5"/>
        <stop offset="1" stop-color="#3176b5" stop-opacity="0.15"/>
      </linearGradient>
    </defs>
    <path d="M293 315 C360 190 470 90 621 0 L640 0 C520 95 450 170 440 235 C435 275 480 300 524 315 Z" fill="url(#blueFade)"/>
    <path d="M379 315 C395 235 420 185 470 140 C445 195 440 245 452 285 L462 315 Z" fill="var(--brand-red)"/>
  </svg>

  <svg class="phone-icon" viewBox="0 0 34 34" aria-hidden="true">
    <path d="M6 14 C6 22 12 28 20 29 L23 25 L18 22 L15 24 C12 22 10 20 9 17 L11 14 L8 9 Z" fill="var(--ink)"/>
    <path d="M17 8 A9 9 0 0 1 26 17 M17 3 A14 14 0 0 1 31 17" fill="none" stroke="var(--ink)" stroke-width="2"/>
  </svg>
  <div class="phone-diagonal">416-555-0143</div>

  <div class="brand-block">
    <div class="brand-mark"></div>
    <div class="brand-name">RN Heating &amp; Cooling</div>
    <div class="brand-tagline">Your trusted HVAC experts</div>
  </div>

  <div class="contact-lines">
    <div>info@rnheatingco-example.net</div>
    <div>www.rnheatingco-example.net</div>
  </div>

  <div class="follow-block">
    <div class="follow-title">Follow us</div>
    <div class="social-list">
      <span class="social-item">Friendloop</span>
      <span class="social-item">Pictavo</span>
    </div>
  </div>
</section>

<section class="back-wrap" aria-label="Rear doors wrap">
  <div class="brand-mark"></div>
  <div class="brand-name">RN Heating &amp; Cooling</div>
  <div class="brand-tagline">Your trusted HVAC experts</div>
  <div class="phone-pill">416-555-0143</div>
  <div class="licence-number">QPLB # 000817264</div>
</section>

</body>
</html>
```